Logo and business card for optometric practice
Curtis Hallorann & Associates
Marta Pelovska, O.D.
Oscar Tremwitz, O.D.
Neil Borromi, O.D.
417 Pembrook Parkway
Larkmere Falls, New York 10987
555-902-4471

Target Market(s)

Patients, general public

Industry/Entity Type

Business

Logo Text

Curtis Hallorann & Associates Optometrists

Logo styles of interest
Pictorial/Combination Logo
Font styles to use
Serif
Sans Serif

Requirements
Must have
• current inspiration: realistic or photo closeup of eye, with interesting treatment of the iris OR
tech look, with closeup of eye and grid like the doctor is looking through a camera or microscope to view the eye up close
Should not have
• NO cartoons

```html
<!DOCTYPE html>
<html lang="en">
<head>
<meta charset="utf-8">
<title>Curtis Hallorann &amp; Associates – Business Card</title>
<link rel="stylesheet" href="https://fonts.googleapis.com/css2?family=Josefin+Sans:wght@300;400&display=swap">
<style>
  :root {
    --brand-blue: #27a8e0;
    --card-white: #ffffff;
    --page-bg: #f1f2f4;
    --ink-dark: #1b1b1b;
    --ink-muted: #8a8a8a;
    --card-shadow: rgba(0, 0, 0, 0.12);
  }
  * { box-sizing: border-box; margin: 0; padding: 0; }
  html, body {
    width: 1200px;
    height: 960px;
    overflow: hidden;
    background: var(--page-bg);
    font-family: "Josefin Sans", "Futura", sans-serif;
  }
  .sheet {
    width: 1200px;
    height: 960px;
    display: flex;
    flex-direction: column;
    align-items: center;
    justify-content: center;
    gap: 64px;
  }
  .card {
    width: 640px;
    height: 366px;
    background: var(--card-white);
    box-shadow: 0 10px 30px var(--card-shadow);
    position: relative;
    overflow: hidden;
  }
  /* Front */
  .card-front__band {
    height: 168px;
    background: var(--brand-blue);
    display: flex;
    flex-direction: column;
    align-items: center;
    justify-content: center;
    padding-top: 6px;
  }
  .brand-dot {
    width: 56px;
    height: 56px;
    border-radius: 50%;
    background: var(--card-white);
    margin-bottom: 14px;
  }
  .brand-name {
    color: var(--card-white);
    font-weight: 400;
    font-size: 24px;
    letter-spacing: 0.04em;
    text-transform: uppercase;
    white-space: nowrap;
    line-height: 1.1;
  }
  .brand-sub {
    color: var(--card-white);
    font-weight: 300;
    font-size: 12px;
    letter-spacing: 0.12em;
    text-transform: uppercase;
    margin-top: 3px;
  }
  .card-front__details {
    height: 198px;
    display: flex;
    flex-direction: column;
    align-items: center;
    justify-content: flex-start;
    padding-top: 22px;
    text-align: center;
  }
  .doctor-name {
    color: var(--ink-dark);
    font-weight: 400;
    font-size: 22px;
    margin-bottom: 10px;
  }
  .contact-line {
    color: var(--ink-muted);
    font-weight: 300;
    font-size: 16px;
    line-height: 1.2;
  }
  /* Back */
  .card-back {
    display: flex;
    flex-direction: column;
    align-items: center;
    justify-content: center;
    gap: 18px;
  }
  .card-back .brand-dot {
    width: 120px;
    height: 120px;
    background: var(--brand-blue);
    margin-bottom: 0;
  }
  .card-back .brand-name {
    color: var(--brand-blue);
    font-size: 20px;
  }
</style>
</head>
<body>
  <main class="sheet">
    <section class="card card-front" aria-label="Business card front">
      <div class="card-front__band">
        <span class="brand-dot" aria-hidden="true"></span>
        <p class="brand-name">Curtis Hallorann &amp; Associates</p>
        <p class="brand-sub">Optometry</p>
      </div>
      <div class="card-front__details">
        <p class="doctor-name">Marta Pelovska, O.D.</p>
        <p class="contact-line">417 Pembrook Parkway</p>
        <p class="contact-line">Larkmere Falls, New York 10987</p>
        <p class="contact-line">555-902-4471</p>
      </div>
    </section>

    <section class="card card-back" aria-label="Business card back">
      <span class="brand-dot" aria-hidden="true"></span>
      <p class="brand-name">Curtis Hallorann &amp; Associates</p>
    </section>
  </main>
</body>
</html>
```